Im open to ideas.. I was thinking on my business cards aswell as my logo. a place for my name. email. phone number and abn..

ive attched a file with my business logo. which i dont love the colours.. i was think a dark background with charcoal letters so something along those colour schumes but im open to ideas..

Business

BRL Constructions

```html
<!DOCTYPE html>
<html lang="en">
<head>
<meta charset="UTF-8">
<title>BRL Constructions – Business Card</title>
<link href="https://fonts.googleapis.com/css2?family=Source+Sans+3:wght@400;600;700&display=swap" rel="stylesheet">
<style>
  :root {
    --stage-top: #2b2b2b;
    --stage-bottom: #050505;
    --card-light: #d4d4d4;
    --card-dark: #515151;
    --ink: #1a1a1a;
    --ink-soft: #2a2a2a;
    --brand-grey: #555555;
    --brand-white: #ffffff;
  }
  * { margin: 0; padding: 0; box-sizing: border-box; }
  html, body {
    width: 1200px;
    height: 900px;
    overflow: hidden;
  }
  body {
    position: relative;
    background: linear-gradient(180deg, var(--stage-top) 0%, #1a1a1a 55%, var(--stage-bottom) 100%);
    font-family: "Source Sans 3", "Myriad Pro", Arial, sans-serif;
  }
  .card {
    position: absolute;
    top: 170px;
    width: 347px;
    height: 561px;
    overflow: hidden;
  }
  .card--front {
    left: 259px;
    background: var(--card-light);
    color: var(--ink);
    text-align: center;
  }
  .card--back {
    left: 631px;
    background: var(--card-dark);
  }
  .brand-name {
    position: absolute;
    left: 0;
    right: 0;
    text-align: center;
    font-weight: 700;
    letter-spacing: 1px;
    line-height: 1;
  }
  .card--front .brand-name {
    top: 98px;
    font-size: 30px;
    color: var(--brand-grey);
  }
  .card--back .brand-name {
    top: 280px;
    font-size: 34px;
    color: var(--brand-white);
  }
  .holder-name {
    position: absolute;
    top: 201px;
    left: 0; right: 0;
    font-size: 22px;
    font-weight: 600;
    color: var(--ink);
  }
  .holder-role {
    position: absolute;
    top: 228px;
    left: 0; right: 0;
    font-size: 15px;
    color: var(--ink-soft);
  }
  .abn {
    position: absolute;
    top: 283px;
    left: 0; right: 0;
    font-size: 15px;
    color: var(--ink-soft);
  }
  .abn strong { font-weight: 600; }
  .contact-icons {
    position: absolute;
    top: 343px;
    left: 0; right: 0;
    display: flex;
    justify-content: center;
    gap: 5px;
  }
  .contact-icons svg { width: 18px; height: 18px; }
  .contact-list {
    position: absolute;
    top: 366px;
    left: 0; right: 0;
    list-style: none;
    font-size: 15px;
    line-height: 25.5px;
    color: var(--ink-soft);
  }
</style>
</head>
<body>
  <section class="card card--front" aria-label="Business card front">
    <div class="brand-name">BRL Constructions</div>
    <h1 class="holder-name">Daniel Harper</h1>
    <p class="holder-role">Managing Director</p>
    <p class="abn"><strong>ABN:</strong>7654321</p>

    <div class="contact-icons" aria-hidden="true">
      <svg viewBox="0 0 18 18" class="icon-phone">
        <path d="M2 6c0-2 3-3 7-3s7 1 7 3v1.5h-3.5V6c-1-.6-2.2-.8-3.5-.8S6.5 5.4 5.5 6v1.5H2z" fill="#1a1a1a"/>
        <path d="M5 8h8l2 7H3z" fill="#1a1a1a"/>
        <circle cx="9" cy="11.5" r="2" fill="#d4d4d4"/>
      </svg>
      <svg viewBox="0 0 18 18" class="icon-mail">
        <rect x="1.5" y="4" width="15" height="10" fill="#1a1a1a"/>
        <path d="M2 4.5 9 10l7-5.5M2 13.5l5-4.5M16 13.5l-5-4.5" stroke="#d4d4d4" stroke-width="1" fill="none"/>
      </svg>
      <svg viewBox="0 0 18 18" class="icon-web">
        <circle cx="9" cy="9" r="7.5" fill="#1a1a1a"/>
        <ellipse cx="9" cy="9" rx="3.2" ry="7.5" fill="none" stroke="#d4d4d4" stroke-width="1"/>
        <path d="M1.5 9h15M3 5h12M3 13h12" stroke="#d4d4d4" stroke-width="1"/>
      </svg>
    </div>

    <ul class="contact-list">
      <li>043-555 218 604</li>
      <li>hello@brlbuild.com</li>
      <li>www.brlbuild.com</li>
    </ul>
  </section>

  <section class="card card--back" aria-label="Business card back">
    <div class="brand-name">BRL Constructions</div>
  </section>
</body>
</html>
```